Letterhead - Quarrington Law Group

I receive a fantastic logo from you guys and I'd like to incorporate it into business cards and letterhead. I accidentally approved design No. 32361474 and contacted designer Ravindra, and Ravindra sent me the zip folder for Design No. 32361417, which I very much appreciate.
I'd like to order business cards and letterhead with Design No. 32361417 as soon as possible, but I want to make sure that you incorporate the correct design (attached). I'd also like to provide my information to add (address, phone number, email, fax) but I'm not quite sure how to do it.
The information that I would like on the business cards and letterhead is as follows:
Quarrington Law Group
Theodore K. Quarrington, Esq.
2741 Hollis Avenue, Suite 520
San Francisco, CA 94087
Office: (415) 378-6130
Fax: (415) 746-0183
ted@quarringtonlawgroup-example.com
Thanks in advance for any guidance.
Ted Quarrington
Quarrington Law Group
(415) 831-4497 (cell)

```html
<!DOCTYPE html>
<html lang="en">
<head>
<meta charset="utf-8">
<title>Quarrington Law Group – Business Card</title>
<link rel="stylesheet" href="https://fonts.googleapis.com/css2?family=Montserrat:wght@300;400;600;700&display=swap">
<style>
  :root {
    --stage: #e9edf1;
    --paper: #ffffff;
    --pattern-light: #f6f7f9;
    --pattern-dark: #eceef2;
    --band: #2f2d2d;
    --accent: #2a8fcf;
    --ink: #2b2b2b;
    --ink-soft: #3a3a3a;
    --on-band: #ffffff;
    --on-band-soft: #d9d9d9;
  }
  * { box-sizing: border-box; margin: 0; padding: 0; }
  html, body { width: 1200px; height: 800px; overflow: hidden; }
  body {
    background: var(--stage);
    font-family: "Montserrat", Arial, sans-serif;
    color: var(--ink);
    position: relative;
  }
  .card {
    position: absolute;
    left: 300px;
    width: 600px;
    height: 340px;
    background: var(--paper);
    box-shadow: 0 10px 28px rgba(20, 40, 70, 0.18);
    overflow: hidden;
  }
  .card--front { top: 30px; }
  .card--back { top: 420px; }
  .card__pattern {
    position: absolute;
    inset: 0;
    background: linear-gradient(135deg, var(--pattern-light) 0%, var(--pattern-dark) 50%, var(--pattern-light) 100%);
  }
  .card__band {
    position: absolute;
    left: 0; top: 0;
    width: 100%; height: 125px;
    background: var(--band);
  }
  .card__stripe {
    position: absolute;
    left: 0; top: 125px;
    width: 100%; height: 30px;
    background: var(--accent);
  }
  .holder {
    position: absolute;
    left: 42px; top: 52px;
  }
  .holder__name {
    font-weight: 700;
    font-size: 27px;
    color: var(--on-band);
    letter-spacing: 0.2px;
  }
  .holder__cell {
    margin-top: 6px;
    display: flex;
    align-items: center;
    gap: 8px;
    font-weight: 300;
    font-size: 14px;
    color: var(--on-band-soft);
  }
  .contacts {
    position: absolute;
    left: 42px; top: 176px;
    list-style: none;
  }
  .contacts__item {
    display: flex;
    align-items: center;
    gap: 8px;
    font-size: 13.5px;
    font-weight: 400;
    line-height: 21px;
    color: var(--ink-soft);
  }
  .address {
    position: absolute;
    left: 42px; top: 246px;
    display: flex;
    gap: 8px;
    font-style: normal;
  }
  .address__lines {
    font-size: 13.5px;
    line-height: 19px;
    color: var(--ink-soft);
  }
  .icon { width: 13px; height: 13px; flex: none; fill: var(--accent); }
  .firm-mark {
    position: absolute;
    right: 34px; bottom: 78px;
    display: flex;
    align-items: center;
    gap: 8px;
    font-size: 17px;
    font-weight: 600;
    color: var(--ink);
  }
  .firm-mark__square {
    width: 12px; height: 12px;
    background: var(--accent);
  }
  .back__message {
    position: absolute;
    left: 0; right: 0; top: 150px;
    text-align: center;
    font-weight: 300;
    font-size: 22px;
    letter-spacing: 0.4px;
    color: var(--ink);
  }
</style>
</head>
<body>

<section class="card card--front">
  <div class="card__pattern" role="img" aria-label="Faint light grey geometric cube pattern across the card"></div>
  <div class="card__band"></div>
  <div class="card__stripe"></div>

  <div class="holder">
    <h1 class="holder__name">Ted Quarrington</h1>
    <p class="holder__cell">
      <svg class="icon" viewBox="0 0 12 16" aria-hidden="true"><path d="M2 0h8a2 2 0 0 1 2 2v12a2 2 0 0 1-2 2H2a2 2 0 0 1-2-2V2a2 2 0 0 1 2-2zm0 2v10h8V2H2zm4 11a1 1 0 1 0 0 2 1 1 0 0 0 0-2z"/></svg>
      (415) 831-4497 (cell)
    </p>
  </div>

  <ul class="contacts">
    <li class="contacts__item">
      <svg class="icon" viewBox="0 0 16 16" aria-hidden="true"><path d="M0 3h4v12H0zM5 4h11v11H5zm2 2v3h7V6zm0 5v2h2v-2zm3 0v2h2v-2zm3 0v2h1v-2z"/></svg>
      (415) 378-6130
    </li>
    <li class="contacts__item">
      <svg class="icon" viewBox="0 0 16 16" aria-hidden="true"><path d="M5 0h8v5h3v11H0V5h5zm2 2v3h4V2zM2 8v6h2V8zm4 0v2h2V8zm3 0v2h2V8zm3 0v2h2V8zm-6 3v2h2v-2zm3 0v2h2v-2zm3 0v2h2v-2z"/></svg>
      (415) 746-0183
    </li>
    <li class="contacts__item">
      <svg class="icon" viewBox="0 0 16 12" aria-hidden="true"><path d="M0 0h16v12H0zm1.5 1.5 6.5 5 6.5-5v-.1H1.5zm-.1 1.8v7.3h13.2V3.3L8 8.4z"/></svg>
      ted@quarringtonlawgroup-example.com
    </li>
  </ul>

  <address class="address">
    <svg class="icon" viewBox="0 0 12 16" aria-hidden="true"><path d="M6 0a6 6 0 0 1 6 6c0 4.5-6 10-6 10S0 10.5 0 6a6 6 0 0 1 6-6zm0 3.5a2.5 2.5 0 1 0 0 5 2.5 2.5 0 0 0 0-5z"/></svg>
    <div class="address__lines">
      Quarrington Law Group<br>
      Theodore K. Quarrington, Esq.<br>
      2741 Hollis Avenue, Suite 520<br>
      San Francisco, CA 94087
    </div>
  </address>

  <div class="firm-mark">
    <span class="firm-mark__square"></span>
    <span class="firm-mark__name">Quarrington Law Group</span>
  </div>
</section>

<section class="card card--back">
  <div class="card__pattern" role="img" aria-label="Faint light grey geometric cube pattern across the card"></div>
  <p class="back__message">Thanks in advance for any guidance.</p>
</section>

</body>
</html>
```